Real Estate Agent needs business card design

We have logo designed already, want to have business card designed. Very interested in those smaller size business card as they look very trendy. Business name is called VORENDA REALTY

```html
<!DOCTYPE html>
<html lang="en">
<head>
<meta charset="utf-8">
<title>Vorenda Realty – Business Card</title>
<link rel="stylesheet" href="https://fonts.googleapis.com/css2?family=Cormorant+SC:wght@500&family=Alegreya+SC:wght@500&family=Source+Sans+3:wght@400&display=swap">
<style>
  :root {
    --backdrop: #070707;
    --card-white: #ffffff;
    --gold: #c39c66;
    --gold-deep: #bf904f;
    --ink: #231f20;
    --text: #2b2b2b;
    --rule: #3a3a3a;
  }
  * { margin: 0; padding: 0; box-sizing: border-box; }
  html, body {
    width: 1200px;
    height: 900px;
    overflow: hidden;
    background: var(--backdrop);
  }
  .stage {
    position: relative;
    width: 1200px;
    height: 900px;
  }
  .card {
    position: absolute;
    top: 306px;
    width: 440px;
    height: 271px;
  }
  .card--front { left: 149px; background: var(--card-white); }
  .card--back { left: 608px; }

  .brand {
    position: absolute;
    left: 36px;
    top: 92px;
    width: 196px;
    text-align: center;
  }
  .brand__square {
    display: block;
    width: 34px;
    height: 34px;
    margin: 0 auto 22px;
    background: var(--gold);
  }
  .brand__name {
    font-family: "Cormorant SC", Georgia, serif;
    font-weight: 500;
    font-size: 27px;
    letter-spacing: 0.5px;
    color: var(--ink);
    white-space: nowrap;
  }
  .divider {
    position: absolute;
    left: 237px;
    top: 76px;
    width: 1px;
    height: 118px;
    background: var(--rule);
  }
  .details {
    position: absolute;
    left: 254px;
    top: 74px;
    font-family: "Source Sans 3", Arial, sans-serif;
    color: var(--text);
    font-size: 12.5px;
    line-height: 16px;
  }
  .details__name {
    font-family: "Alegreya SC", Georgia, serif;
    font-weight: 500;
    font-size: 19px;
    line-height: 22px;
    color: var(--gold-deep);
  }
  .details__role { margin-bottom: 9px; }
  .details__address { margin-bottom: 9px; }
  .contact {
    display: flex;
    align-items: center;
    gap: 5px;
  }
  .contact svg { width: 10px; height: 10px; flex: none; }

  .pattern-field {
    position: absolute;
    inset: 0;
    background: linear-gradient(135deg, #c6a06a, #c09a63);
  }
  .back-name {
    position: absolute;
    left: 0;
    right: 0;
    top: 165px;
    text-align: center;
    font-family: "Cormorant SC", Georgia, serif;
    font-weight: 500;
    font-size: 18px;
    color: var(--card-white);
    letter-spacing: 0.5px;
  }
</style>
</head>
<body>
<main class="stage">
  <section class="card card--front">
    <div class="brand">
      <span class="brand__square"></span>
      <p class="brand__name">Vorenda Realty</p>
    </div>
    <div class="divider"></div>
    <div class="details">
      <p class="details__name">Clara Wenham</p>
      <p class="details__role">Senior Property Consultant</p>
      <p class="details__address">7C, 148 Harbour Parade,<br>North Vale, NSW 2071</p>
      <p class="contact">
        <svg viewBox="0 0 10 10" aria-hidden="true"><path fill="#c39c66" d="M2.2 0.6l1.5 1.8-0.8 1.2c0.6 1.3 1.5 2.2 2.8 2.8l1.2-0.8 1.8 1.5-0.6 1.6C4.6 8.6 1.4 5.4 0.6 1.2z"/></svg>
        <span>0491 552 317</span>
      </p>
      <p class="contact">
        <svg viewBox="0 0 10 10" aria-hidden="true"><circle cx="5" cy="5" r="4.6" fill="#c39c66"/><path d="M0.6 5h8.8M5 0.4c-2 2.5-2 6.7 0 9.2M5 0.4c2 2.5 2 6.7 0 9.2" stroke="#fff" stroke-width="0.7" fill="none"/></svg>
        <span>www.vorendarealty.com.au</span>
      </p>
    </div>
  </section>

  <section class="card card--back">
    <div class="pattern-field" role="img" aria-label="Repeating brand monogram pattern in soft tone-on-tone gold"></div>
    <p class="back-name">Vorenda Realty</p>
  </section>
</main>
</body>
</html>
```